BrookPine Lending Needs a Stated Income Flyer

We need a flyer created for our Stated Income loan program, using the color scheme to match our company logo.
I've included a stock photo to be used and within that photo, we want Funded stamped in red on the blank poster board.
For the written part of the flyer, we want the word State Income in red.
On the bottom part (Contact Us), we want to make it possible for us to edit for any future loan officer we hire along the way to include their contact information.
We like the flyer for TorvaCredit.

```html
<!DOCTYPE html>
<html lang="en">
<head>
<meta charset="utf-8">
<title>BrookPine Lending – Stated Income Flyer</title>
<link rel="stylesheet" href="https://fonts.googleapis.com/css2?family=PT+Serif:wght@400;700&family=Stardos+Stencil:wght@700&display=swap">
<style>
  :root {
    --navy: #1f4a8c;
    --navy-dark: #173a70;
    --red: #d0202f;
    --ink: #2b2b2b;
    --band: #d9d8d3;
    --body-light: #f1f0ec;
    --body-mid: #e4e3de;
    --page: #f4f4f4;
  }
  * { box-sizing: border-box; margin: 0; padding: 0; }
  html, body { width: 1200px; height: 900px; overflow: hidden; background: var(--page); }
  body { position: relative; font-family: "PT Serif", Georgia, serif; color: var(--ink); }

  .flyer {
    position: absolute; left: 300px; top: 20px; width: 600px; height: 860px;
    background: linear-gradient(180deg, var(--body-light), var(--body-mid));
    box-shadow: 0 6px 24px rgba(0,0,0,.18); overflow: hidden;
  }
  .header { position: absolute; left: 0; top: 0; width: 600px; height: 140px; background: var(--band); }
  .brand { position: absolute; top: 40px; width: 100%; display: flex; justify-content: center; align-items: center; gap: 12px; }
  .brand-mark { width: 34px; height: 34px; border-radius: 50%; background: var(--navy); }
  .brand-name { font-size: 34px; font-weight: 700; color: var(--navy); letter-spacing: .5px; }

  .photo {
    position: absolute; left: 0; top: 118px; width: 600px; height: 340px;
    background: linear-gradient(100deg, #e8c7b8 0%, #b9a89a 25%, #ede6dc 45%, #a7b6cc 70%, #2c2f3a 100%);
  }
  .board {
    position: absolute; left: 86px; top: 262px; width: 264px; height: 150px; background: #f7f7f5;
    display: flex; align-items: center; justify-content: center;
  }
  .stamp {
    font-family: "Stardos Stencil", "Impact", sans-serif; font-weight: 700; font-size: 54px;
    color: var(--red); letter-spacing: 2px; transform: rotate(-9deg);
  }
  .waves { position: absolute; left: 0; top: 0; width: 600px; height: 860px; pointer-events: none; }

  .title-stated, .title-income { position: absolute; color: var(--red); font-weight: 400; line-height: 1; }
  .title-stated { left: 100px; top: 468px; font-size: 38px; }
  .title-income { left: 30px; top: 510px; font-size: 38px; }
  .title-rule { position: absolute; left: 100px; top: 506px; width: 476px; height: 3px; background: var(--red); }
  .fast-easy { position: absolute; left: 208px; top: 512px; font-size: 12px; line-height: 1.05; color: var(--ink); }

  .offer { position: absolute; right: 24px; top: 516px; text-align: right; }
  .offer-head { font-size: 20px; font-weight: 700; color: var(--navy); line-height: 1.2; letter-spacing: .3px; }
  .offer-line { font-size: 17px; line-height: 1.45; color: var(--ink); }
  .offer-note { font-size: 11px; color: #555; margin-top: 2px; }

  .checklist { position: absolute; list-style: none; font-size: 12px; line-height: 1.15; }
  .checklist li { position: relative; padding-left: 20px; margin-bottom: 7px; }
  .checklist svg { position: absolute; left: 0; top: 1px; width: 13px; height: 12px; }
  .checklist-no { left: 32px; top: 562px; width: 210px; }
  .checklist-terms { left: 248px; top: 620px; width: 260px; }

  .rates { position: absolute; left: 0; top: 745px; width: 600px; display: flex; justify-content: center; gap: 12px; align-items: center; }
  .rates-text { text-align: center; }
  .rates-head { font-size: 22px; font-weight: 700; color: var(--navy); letter-spacing: .3px; }
  .rates-sub { font-size: 12px; color: var(--ink); }

  .footer { position: absolute; left: 0; top: 790px; width: 600px; height: 70px; background: var(--band); }
  .officer-name { position: absolute; left: 32px; top: 24px; font-size: 16px; font-weight: 700; color: #444; letter-spacing: .5px; }
  .officer-contact { position: absolute; right: 28px; top: 16px; font-size: 11.5px; line-height: 1.5; color: #444; }
</style>
</head>
<body>
<main class="flyer">
  <header class="header">
    <div class="brand"><span class="brand-mark"></span><span class="brand-name">BrookPine Lending</span></div>
  </header>

  <section class="photo" role="img" aria-label="Stock photo of a cheering group of business people holding up a blank poster board"></section>
  <div class="board"><span class="stamp">FUNDED</span></div>

  <svg class="waves" viewBox="0 0 600 860" aria-hidden="true">
    <path d="M0 130 C120 110 220 150 330 128 C430 108 510 112 600 135 L600 118 L0 118 Z" fill="var(--band)"/>
    <path d="M0 130 C120 110 220 150 330 128 C430 108 510 112 600 135" fill="none" stroke="var(--navy)" stroke-width="5"/>
    <path d="M0 428 C110 452 230 418 340 438 C440 456 520 430 600 418 L600 470 L0 470 Z" fill="var(--body-light)"/>
    <path d="M0 428 C110 452 230 418 340 438 C440 456 520 430 600 418" fill="none" stroke="var(--navy)" stroke-width="5"/>
  </svg>

  <h1 class="title-stated">STATED</h1>
  <div class="title-rule"></div>
  <h1 class="title-income">INCOME</h1>
  <div class="fast-easy">FAST &amp;<br>EASY</div>

  <div class="offer">
    <div class="offer-head">PURCHASE &amp;<br>CASH OUT REFINANCE</div>
    <div class="offer-line">Non-owner SFR/Condo/2-4 Units</div>
    <div class="offer-line">5+ Units &amp; Commercial</div>
    <div class="offer-note">– Ask for Details</div>
  </div>

  <ul class="checklist checklist-no">
    <li><svg viewBox="0 0 13 12"><path d="M1 6 L5 10 L12 1" fill="none" stroke="#333" stroke-width="2"/></svg>NO Tax Returns</li>
    <li><svg viewBox="0 0 13 12"><path d="M1 6 L5 10 L12 1" fill="none" stroke="#333" stroke-width="2"/></svg>NO 4506-T</li>
    <li><svg viewBox="0 0 13 12"><path d="M1 6 L5 10 L12 1" fill="none" stroke="#333" stroke-width="2"/></svg>NO Cash-Out Restrictions</li>
    <li><svg viewBox="0 0 13 12"><path d="M1 6 L5 10 L12 1" fill="none" stroke="#333" stroke-width="2"/></svg>NO Cash Reserves Required</li>
    <li><svg viewBox="0 0 13 12"><path d="M1 6 L5 10 L12 1" fill="none" stroke="#333" stroke-width="2"/></svg>NO Limit on Number of<br>Properties owned or financed</li>
    <li><svg viewBox="0 0 13 12"><path d="M1 6 L5 10 L12 1" fill="none" stroke="#333" stroke-width="2"/></svg>NO DTI Calculation</li>
    <li><svg viewBox="0 0 13 12"><path d="M1 6 L5 10 L12 1" fill="none" stroke="#333" stroke-width="2"/></svg>NO Seasoned Funds –<br>No Asset Disclosures (Purchase)</li>
  </ul>

  <ul class="checklist checklist-terms">
    <li><svg viewBox="0 0 13 12"><path d="M1 6 L5 10 L12 1" fill="none" stroke="#333" stroke-width="2"/></svg>Max Rebate 2%</li>
    <li><svg viewBox="0 0 13 12"><path d="M1 6 L5 10 L12 1" fill="none" stroke="#333" stroke-width="2"/></svg>Max 70% Loan-to-value</li>
    <li><svg viewBox="0 0 13 12"><path d="M1 6 L5 10 L12 1" fill="none" stroke="#333" stroke-width="2"/></svg>650 Min Credit Score</li>
    <li><svg viewBox="0 0 13 12"><path d="M1 6 L5 10 L12 1" fill="none" stroke="#333" stroke-width="2"/></svg>Loan Amounts $100,000 to $2,000,000</li>
    <li><svg viewBox="0 0 13 12"><path d="M1 6 L5 10 L12 1" fill="none" stroke="#333" stroke-width="2"/></svg>Lending to Corporations, LLC,<br>Partnership &amp; Individuals</li>
  </ul>

  <div class="rates">
    <svg width="40" height="36" viewBox="0 0 40 36" aria-hidden="true">
      <path d="M4 17 L20 3 L36 17" fill="none" stroke="var(--navy)" stroke-width="3"/>
      <rect x="9" y="16" width="22" height="18" fill="none" stroke="var(--navy)" stroke-width="3"/>
      <path d="M14 24 L19 29 L28 18" fill="none" stroke="var(--navy)" stroke-width="3"/>
    </svg>
    <div class="rates-text">
      <div class="rates-head">RATES AS LOW AS 6.49%</div>
      <div class="rates-sub">3 &amp; 5 Year Fixed ARM – 30 Year Amortization</div>
    </div>
  </div>

  <footer class="footer">
    <div class="officer-name">MARCUS DELANE</div>
    <div class="officer-contact">888-555-0142 &nbsp;|&nbsp; marcus@brookpinelending.com<br>BRE #01987342</div>
  </footer>
</main>
</body>
</html>
```